Re-branding stationary for Company

Corvane Diamonds is a diamond trading company that has been established since more then 30years.

We are currently looking to re-design our current logo design into something more modern and more appealing the the new generation. Small changes are what we are looking for that will give our company a little more modern look and a new appeal.
The design should be on similar lines to what our current logo is, but we are definitely wanting to have some modern changes to this.
Along with this, we are looking to have design for complete stationary including, business cards, envelopes, letterheads, etc..

Attached is our current logo, can use this as a base point towards creating a new design.
Updates

Project Deadline Extended Reason: Am still looking for wonderful and amazingly creative design for my company, a facelift with a little modern touchHave provided you with a current logo of the company as inspiration to make something new and unique. PLEASE DO NOT USE COPY THE LOGO FILE AS IT IS! Added Wednesday, May 6, 2015

Target Market(s)

We are a company established since over 30 years, and want to maintain our core fundamental values which is portrayed through our logo. Use this as a base into creating new modern design.

Industry/Entity Type

It Company

Font styles to use
Serif
Sans Serif
Decorative
Script

Requirements
Must have
• A modern touch
• Color combination should be similar in terms with what we currently use in attached design.
Nice to have
• Want that the design is appealing using simple but yet modern features to change and restructure the current company logo.
Should not have
• Not looking more multi colored design
• Not gotta be too overly extravagant

```html
<!DOCTYPE html>
<html lang="en">
<head>
<meta charset="UTF-8">
<title>Corvane Diamonds – Business Card</title>
<link rel="stylesheet" href="https://fonts.googleapis.com/css2?family=Cinzel:wght@400;500&display=swap">
<style>
  :root {
    --backdrop: #e4e5e7;
    --card-blue: #0b56a8;
    --ink-white: #ffffff;
    --card-shadow: rgba(0, 0, 0, 0.22);
  }

  * { margin: 0; padding: 0; box-sizing: border-box; }

  html, body {
    width: 1200px;
    height: 798px;
    overflow: hidden;
    background: var(--backdrop);
  }

  .stage {
    position: relative;
    width: 1200px;
    height: 798px;
    display: flex;
    align-items: center;
    justify-content: center;
  }

  .business-card {
    position: relative;
    width: 840px;
    height: 480px;
    background: var(--card-blue);
    color: var(--ink-white);
    font-family: "Cinzel", serif;
    box-shadow: 0 14px 34px var(--card-shadow);
  }

  .company-name {
    position: absolute;
    top: 62px;
    left: 0;
    right: 0;
    text-align: center;
    font-size: 54px;
    font-weight: 400;
    letter-spacing: 1px;
    line-height: 1;
  }

  .divider {
    position: absolute;
    top: 160px;
    left: 0;
    width: 100%;
    height: 24px;
  }

  .person {
    position: absolute;
    top: 248px;
    left: 0;
    right: 0;
    text-align: center;
  }

  .person-name {
    font-size: 60px;
    font-weight: 400;
    letter-spacing: 1px;
    line-height: 1;
  }

  .person-title {
    margin-top: 14px;
    font-size: 38px;
    font-weight: 400;
    letter-spacing: 1px;
    line-height: 1;
  }
</style>
</head>
<body>
  <main class="stage">
    <section class="business-card">
      <h1 class="company-name">Corvane Diamonds</h1>

      <svg class="divider" viewBox="0 0 840 24" aria-hidden="true">
        <line x1="0" y1="12" x2="840" y2="12" stroke="var(--ink-white)" stroke-width="3"/>
        <circle cx="420" cy="12" r="9" fill="var(--ink-white)"/>
      </svg>

      <div class="person">
        <p class="person-name">Your Name</p>
        <p class="person-title">Job Title</p>
      </div>
    </section>
  </main>
</body>
</html>
```